Kestrel Works Wall Art Design

Our local government has developed a department called the "Kestrel Works" which has been running for a few years. Our purpose is to encourage staff to think Under the Willow and engage their problems in new ways. We offer tools and services which enable collaboration between people and other departments, one such tool is our new meeting room. We've designed this space with the intention of encouraging creativity and allowing staff members to break away from the ordinary working environment. Attached are photos of the room.
The room is called "Under the Willow". In one photo you will see our Under the Willow sign filling the space where'd we'd like to have the design on, however we would like to stay away from naming labels in our design to convey to staff that this is their space as well, rather than the Kestrel Works' special little room. We would like a design that embodies the spirit of our department. We've talked about what that means to us and we've stepped it out as;
Investigate
Collaborate
Innovate
Create
Celebrate
We had ideas of having a funky word jumble design or something creative to use these words, but we'd love to see anything else that conveys a feeling of creativity.
The size of the art is limited to 1400mm x 2800mm

```html
<!DOCTYPE html>
<html lang="en">
<head>
<meta charset="utf-8">
<title>Kestrel Works Wall Art – Create, Celebrate, Investigate</title>
<link rel="stylesheet" href="https://fonts.googleapis.com/css2?family=Archivo+Black&display=swap">
<style>
  :root {
    --backdrop: #ecebe6;
    --panel: #ffffff;
    --panel-shadow: rgba(0, 0, 0, 0.18);
    --create-a: #8a6f5c;
    --create-b: #c9a27e;
    --create-c: #6d7c8a;
    --celebrate-a: #2f7d2a;
    --celebrate-b: #a6cf3a;
    --celebrate-c: #e6d23a;
    --investigate-a: #0b1a4a;
    --investigate-b: #2a6fd6;
    --investigate-c: #9fd0ff;
  }

  html, body {
    margin: 0;
    padding: 0;
    width: 1200px;
    height: 675px;
    overflow: hidden;
    background: var(--backdrop);
  }

  .wall-art {
    position: relative;
    width: 1200px;
    height: 675px;
  }

  .word-panel {
    position: absolute;
    display: flex;
    align-items: center;
    justify-content: center;
    background: var(--panel);
    box-shadow: 0 3px 10px var(--panel-shadow);
  }

  .word-panel__word {
    margin: 0;
    font-family: "Archivo Black", "Arial Black", sans-serif;
    font-weight: 400;
    text-transform: uppercase;
    line-height: 1;
    color: transparent;
    -webkit-background-clip: text;
    background-clip: text;
  }

  .word-panel--create {
    left: 50px;
    top: 296px;
    width: 300px;
    height: 86px;
  }
  .word-panel--create .word-panel__word {
    font-size: 40px;
    letter-spacing: 3px;
    background-image: linear-gradient(100deg, var(--create-a), var(--create-b) 45%, var(--create-c));
  }

  .word-panel--celebrate {
    left: 420px;
    top: 262px;
    width: 330px;
    height: 80px;
  }
  .word-panel--celebrate .word-panel__word {
    font-size: 34px;
    letter-spacing: 3px;
    background-image: linear-gradient(100deg, var(--celebrate-a), var(--celebrate-b) 50%, var(--celebrate-c));
  }

  .word-panel--investigate {
    left: 785px;
    top: 250px;
    width: 370px;
    height: 96px;
  }
  .word-panel--investigate .word-panel__word {
    font-size: 38px;
    letter-spacing: 3px;
    background-image: linear-gradient(100deg, var(--investigate-a), var(--investigate-b) 45%, var(--investigate-c) 70%, var(--investigate-a));
  }
</style>
</head>
<body>
  <main class="wall-art">
    <section class="word-panel word-panel--create">
      <p class="word-panel__word">Create</p>
    </section>
    <section class="word-panel word-panel--celebrate">
      <p class="word-panel__word">Celebrate</p>
    </section>
    <section class="word-panel word-panel--investigate">
      <p class="word-panel__word">Investigate</p>
    </section>
  </main>
</body>
</html>
```